Need a design for Loan Site with new age design

We need a design for our site www.fernpivot.in , we deal with different verticals like home loan, personal loan, loan against property and business loans. Feel free to get in touch if you have any questions.

I have like the concept of the drop down on the eye level where consumer is able to select the product they wish and continue with the form https://www.tallowcrest.com/ . They are in the same line of business as we are.

Here are few more designs which i personally like just to get idea about the taste

https://plumweatherly.com/
http://vexlar.com/partners

Industry/Entity Type

Loan

Number of Pages Required

2 page

Colors
34a7d7
add136
faa54b
fbee3e

Requirements
Must have
• I have like the concept of the drop down on the eye level where consumer is able to select the product they wish and continue with the form https://www.tallowcrest.com/ . They are in the same line of business as we are.
• Here are few more designs which i personally like just to get idea about the taste
• https://plumweatherly.com/
• http://vexlar.com/partners

```html
<!DOCTYPE html>
<html lang="en">
<head>
<meta charset="utf-8">
<title>Fern Pivot – Home</title>
<link rel="stylesheet" href="https://fonts.googleapis.com/css2?family=Lato:ital,wght@0,400;0,700;0,900;1,700&display=swap">
<style>
  :root {
    --blue: #1d6cb5;
    --blue-dark: #0f4f94;
    --blue-deep: #0b3f7a;
    --sky: #2aa8e0;
    --sky-dark: #1a79c3;
    --coral: #f45b5b;
    --coral-light: #ff7b76;
    --ink: #1b5fa8;
    --grey-bg: #eef0f3;
    --white: #ffffff;
    --text-muted: #9aa3ad;
  }
  * { box-sizing: border-box; margin: 0; padding: 0; }
  html, body { width: 918px; height: 1200px; overflow: hidden; background: var(--white); }
  body { font-family: "Lato", sans-serif; position: relative; color: var(--ink); }

  /* Header */
  .site-header { position: absolute; top: 0; left: 0; width: 918px; height: 72px; background: var(--white); z-index: 5; }
  .brand { position: absolute; left: 120px; top: 22px; display: flex; align-items: center; gap: 8px; }
  .brand-mark { width: 30px; height: 30px; background: var(--blue); }
  .brand-name { font-size: 18px; font-weight: 400; color: var(--blue); }
  .brand-divider { position: absolute; left: 250px; top: 18px; width: 2px; height: 38px; background: var(--blue); }
  .main-nav { position: absolute; left: 266px; top: 25px; display: flex; gap: 14px; align-items: center; }
  .main-nav a { font-size: 12px; font-weight: 700; color: var(--blue-dark); text-decoration: none; line-height: 22px; }
  .main-nav a.is-active { background: var(--coral); color: var(--white); padding: 0 11px; border-radius: 5px; }
  .login-icon { position: absolute; left: 778px; top: 22px; }

  /* Hero */
  .hero { position: absolute; top: 72px; left: 0; width: 918px; height: 290px; }
  .hero-backdrop { position: absolute; inset: 0;
    background: linear-gradient(180deg, #d9e6f2 0%, #6d9fcc 22%, #2f76b8 55%, var(--blue) 100%); }
  .hero-title { position: absolute; top: 72px; width: 100%; text-align: center; color: var(--white); font-size: 29px; font-weight: 700; }
  .hero-sub { position: absolute; top: 114px; width: 100%; text-align: center; color: var(--white); font-size: 17px; font-weight: 400; }
  .loan-search { position: absolute; top: 160px; left: 257px; width: 403px; height: 38px; display: flex; border-radius: 3px; overflow: hidden; box-shadow: 0 2px 6px rgba(0,0,0,.2); }
  .loan-search .select { background: var(--white); width: 160px; display: flex; align-items: center; justify-content: space-between; padding: 0 12px; font-size: 11px; color: var(--text-muted); border-right: 1px solid #dfe3e8; }
  .loan-search .btn-search { flex: 1; background: var(--coral); color: var(--white); font-size: 14px; display: flex; align-items: center; justify-content: center; }
  .hero-arrows { position: absolute; top: 200px; left: 320px; }
  .mascot { position: absolute; background: linear-gradient(180deg, #f6c99a 0%, #2d3a5e 60%, #1e2740 100%); border-radius: 60px 60px 20px 20px; }
  .mascot-hero { left: 400px; top: 282px; width: 124px; height: 162px; z-index: 3; }

  .category-band { position: absolute; top: 362px; left: 0; width: 918px; height: 60px; background: var(--coral); }
  .category-band::before { content: ""; position: absolute; left: 0; right: 0; top: 0; height: 8px; background: var(--coral-light); }
  .partners-bg { position: absolute; top: 422px; left: 0; width: 918px; height: 60px; background: linear-gradient(180deg, var(--grey-bg), var(--white)); }

  /* Partners */
  .partners-title { position: absolute; top: 468px; width: 100%; text-align: center; font-size: 23px; font-weight: 700; color: var(--blue); }
  .partners-title em { color: var(--coral); font-style: italic; }
  .partners-rule { position: absolute; top: 506px; left: 240px; width: 438px; height: 1px; background: linear-gradient(90deg, transparent, #c5ccd6, transparent); }
  .partner-list { position: absolute; top: 536px; left: 120px; display: flex; gap: 9px; list-style: none; }
  .partner-card { width: 128px; height: 56px; background: var(--white); box-shadow: 0 2px 8px rgba(0,0,0,.12); display: flex; align-items: center; justify-content: center; font-size: 13px; font-weight: 700; color: var(--blue-dark); }

  /* Features */
  .features-head { position: absolute; top: 648px; left: 0; width: 918px; height: 42px; background: linear-gradient(180deg, var(--blue) 0%, var(--blue-deep) 100%); color: var(--white); text-align: center; font-size: 21px; font-weight: 700; line-height: 42px; z-index: 2; }
  .features-head::after { content: ""; position: absolute; left: 449px; bottom: -10px; border-left: 10px solid transparent; border-right: 10px solid transparent; border-top: 10px solid var(--blue-deep); }
  .features { position: absolute; top: 690px; left: 0; width: 918px; height: 228px; background: linear-gradient(180deg, #d8e9f6 0%, #f4f8fc 50%, #e3eef7 100%); }
  .feature { position: absolute; top: 58px; width: 160px; text-align: center; }
  .feature svg { display: block; margin: 0 auto; }
  .feature h3 { margin-top: 14px; font-size: 13px; font-weight: 700; color: var(--blue-dark); }
  .feature p { font-size: 9px; color: var(--ink); line-height: 11px; }
  .feature-divider { position: absolute; top: 48px; width: 1px; height: 118px; background: #c3d3e2; }
  .mascot-features { left: 400px; top: 18px; width: 124px; height: 204px; }

  /* CTA */
  .cta { position: absolute; top: 918px; left: 0; width: 918px; height: 210px; background: var(--sky); overflow: hidden; }
  .cta-stripe { position: absolute; top: 34px; left: 0; width: 100%; height: 104px; background: var(--sky-dark); }
  .cta-title { position: absolute; top: 50px; left: 360px; width: 340px; text-align: center; color: var(--white); font-size: 23px; font-weight: 700; }
  .btn-inquire { position: absolute; top: 88px; left: 472px; width: 120px; height: 27px; background: var(--coral); color: var(--white); font-size: 14px; text-align: center; line-height: 27px; }
  .cta-fade { position: absolute; left: 0; bottom: 0; width: 100%; height: 80px; background: linear-gradient(180deg, rgba(255,255,255,0), var(--white)); }
  .mascot-cta { left: 180px; top: 6px; width: 180px; height: 204px; border-radius: 90px 90px 20px 20px; }

  /* Footer */
  .site-footer { position: absolute; top: 1128px; left: 0; width: 918px; height: 72px; background: var(--white); }
  .site-footer .brand { left: 154px; top: 20px; }
  .site-footer .brand-mark { width: 22px; height: 22px; }
  .site-footer .brand-name { font-size: 12px; }
  .legal { position: absolute; left: 574px; top: 24px; font-size: 10px; color: var(--blue-dark); font-weight: 700; }
  .legal a { color: var(--sky); text-decoration: none; margin-left: 10px; font-weight: 400; }
</style>
</head>
<body>
  <header class="site-header">
    <div class="brand"><span class="brand-mark"></span><span class="brand-name">Fern Pivot</span></div>
    <span class="brand-divider"></span>
    <nav class="main-nav">
      <a class="is-active" href="#">Home</a>
      <a href="#">Who We Are</a>
      <a href="#">Services</a>
      <a href="#">Blog</a>
      <a href="#">Career</a>
      <a href="#">Reach Us</a>
    </nav>
    <svg class="login-icon" width="26" height="28" viewBox="0 0 26 28" aria-label="Log in">
      <path d="M8 4 V2 H24 V26 H8 V24" fill="none" stroke="var(--blue-dark)" stroke-width="3"/>
      <path d="M2 14 H16 M11 8 L17 14 L11 20" fill="none" stroke="var(--blue-dark)" stroke-width="3.5"/>
    </svg>
  </header>

  <section class="hero">
    <div class="hero-backdrop" role="img" aria-label="Blue sky framed by soft clouds with a faint pattern of money and finance symbols"></div>
    <h1 class="hero-title">Looking for a secured or unsecured loan</h1>
    <p class="hero-sub">We will help you get the best interest rate</p>
    <div class="loan-search">
      <div class="select">I would like to
        <svg width="12" height="8" viewBox="0 0 12 8"><path d="M1 1 L6 6 L11 1" fill="none" stroke="var(--coral)" stroke-width="2"/></svg></div>
      <div class="select">Select a Product
        <svg width="12" height="8" viewBox="0 0 12 8"><path d="M1 1 L6 6 L11 1" fill="none" stroke="var(--coral)" stroke-width="2"/></svg></div>
      <div class="btn-search">Search</div>
    </div>
    <svg class="hero-arrows" width="280" height="90" viewBox="0 0 280 90" aria-hidden="true">
      <path d="M40 86 C 20 60, 18 30, 30 10 M22 18 L30 8 L38 18" fill="none" stroke="#fff" stroke-width="2"/>
      <path d="M240 86 C 260 60, 262 30, 250 10 M242 18 L250 8 L258 18" fill="none" stroke="#fff" stroke-width="2"/>
    </svg>
  </section>
  <div class="category-band"></div>
  <div class="partners-bg"></div>
  <div class="mascot mascot-hero" role="img" aria-label="Cheerful cartoon businessman in a suit with arms raised"></div>

  <h2 class="partners-title">We work with all <em>Premium Financial Institutions</em></h2>
  <div class="partners-rule"></div>
  <ul class="partner-list">
    <li class="partner-card">Halvern Bank</li>
    <li class="partner-card">Corvista Bank</li>
    <li class="partner-card">Tessmark Bank</li>
    <li class="partner-card">Brindle Finserv</li>
    <li class="partner-card">Oakhurst</li>
  </ul>

  <h2 class="features-head">Features</h2>
  <section class="features">
    <div class="feature" style="left:94px">
      <svg width="64" height="76" viewBox="0 0 64 76"><rect x="4" y="8" width="56" height="66" rx="4" fill="none" stroke="var(--blue)" stroke-width="4"/><rect x="20" y="2" width="24" height="12" rx="3" fill="var(--blue)"/><circle cx="32" cy="32" r="7" fill="var(--blue)"/><path d="M20 50 Q32 36 44 50Z" fill="var(--blue)"/><path d="M14 60 H50 M14 66 H42" stroke="var(--blue)" stroke-width="3"/></svg>
      <h3>Easy Documentation</h3>
    </div>
    <div class="feature" style="left:244px">
      <svg width="86" height="76" viewBox="0 0 86 76"><rect x="4" y="26" width="44" height="34" fill="var(--blue)"/><path d="M48 36 H68 L80 50 V60 H48Z" fill="var(--blue)"/><circle cx="20" cy="64" r="8" fill="var(--blue)" stroke="#fff" stroke-width="3"/><circle cx="64" cy="64" r="8" fill="var(--blue)" stroke="#fff" stroke-width="3"/><circle cx="22" cy="18" r="14" fill="#fff" stroke="var(--blue)" stroke-width="4"/><path d="M22 10 V18 H29" stroke="var(--blue)" stroke-width="3" fill="none"/></svg>
      <h3>Doorstep Deliveries</h3>
    </div>
    <div class="feature-divider" style="left:250px"></div>
    <div class="feature" style="left:502px">
      <svg width="76" height="80" viewBox="0 0 76 80"><rect x="4" y="4" width="40" height="50" rx="3" fill="none" stroke="var(--blue)" stroke-width="4"/><rect x="30" y="26" width="40" height="50" rx="3" fill="#fff" stroke="var(--blue)" stroke-width="4"/><path d="M10 28 H30 M24 22 L30 28 L24 34" stroke="var(--blue)" stroke-width="3" fill="none"/><path d="M64 52 H44 M50 46 L44 52 L50 58" stroke="var(--blue)" stroke-width="3" fill="none"/></svg>
      <h3>Compare Quote</h3>
      <p>from all major<br>financial institutions</p>
    </div>
    <div class="feature-divider" style="left:654px"></div>
    <div class="feature" style="left:654px">
      <svg width="76" height="80" viewBox="0 0 76 80"><rect x="6" y="8" width="48" height="64" rx="3" fill="none" stroke="var(--blue)" stroke-width="4"/><rect x="20" y="2" width="20" height="10" rx="3" fill="var(--blue)"/><path d="M14 28 l3 3 l5 -6 M28 28 H44 M14 42 l3 3 l5 -6 M28 42 H44 M14 56 H34" stroke="var(--blue)" stroke-width="3" fill="none"/><circle cx="56" cy="60" r="15" fill="var(--blue)" stroke="#fff" stroke-width="3"/><path d="M49 60 l5 5 l9 -10" stroke="#fff" stroke-width="3.5" fill="none"/></svg>
      <h3>Get Approval</h3>
      <p>within 7 business days</p>
    </div>
    <div class="mascot mascot-features" role="img" aria-label="Cartoon businessman with glasses waving both hands"></div>
  </section>

  <section class="cta">
    <div class="cta-stripe"></div>
    <div class="cta-fade"></div>
    <div class="mascot mascot-cta" role="img" aria-label="Cartoon businessman leaping out of the clouds and waving"></div>
    <h2 class="cta-title">What Are You Waiting For?</h2>
    <a class="btn-inquire">Inquire Now</a>
  </section>

  <footer class="site-footer">
    <div class="brand"><span class="brand-mark"></span><span class="brand-name">Fern Pivot</span></div>
    <p class="legal">Copyright © 2016 Fern Pivot <a href="#">Privacy Policy</a></p>
  </footer>
</body>
</html>
```